Funeral Services Site

We need a website for a Funeral Services company. The old website is: www.rouwcentrumkorvelaer.be We need the same structure and text.

Target Market(s)

Customers.

Coding

Coded - Design and coding required

Number of Pages Required

4 page

Font styles to use
Serif
Sans Serif
Script

```html
<!DOCTYPE html>
<html lang="nl">
<head>
<meta charset="utf-8">
<title>Rouwcentrum Verhaegen</title>
<link href="https://fonts.googleapis.com/css2?family=Karla:wght@400;500;700&family=Roboto:wght@400;500&display=swap" rel="stylesheet">
<style>
:root{
  --page:#e4e0df;
  --white:#ffffff;
  --ink:#1c1c1c;
  --muted:#555555;
  --rule:#c9c9c9;
  --dark-btn:#2c2c2c;
  --light-btn:#cfcdcd;
  --slate:#3d3d3f;
  --sky:#6f9ccb;
  --footer:#000000;
}
*{margin:0;padding:0;box-sizing:border-box}
html,body{width:1200px;height:2392px;overflow:hidden;background:var(--page)}
body{position:relative;font-family:'Karla',sans-serif;color:var(--ink)}
.abs{position:absolute}
.flags{top:16px;left:990px;display:flex;gap:12px}
.flag{width:22px;height:15px;display:flex;flex-direction:column}
.flag.nl span{flex:1}
.flag.fr{flex-direction:row}
.flag.fr span{flex:1}
.site{position:absolute;left:150px;top:49px;width:900px;height:2240px;background:var(--white);overflow:hidden}
.site .abs{position:absolute}
.brand-mark{width:92px;height:92px;border-radius:50%;background:var(--ink)}
.brand-name{font-weight:500;color:var(--ink);letter-spacing:1px;white-space:nowrap}
.contact-main{font-size:22px;font-weight:500;letter-spacing:1px;line-height:1}
.contact-sub{font-size:16px;line-height:1}
.ornament{background:#d9d9d9;border-radius:4px}
.rule{height:1px;background:var(--rule)}
.nav{top:252px;left:0;width:900px;display:flex;font-size:15px;color:var(--muted);letter-spacing:.4px}
.nav a{position:absolute;color:inherit;text-decoration:none;white-space:nowrap}
.nav a.active{color:var(--ink)}
.hero{top:294px;left:0;width:900px;height:400px;background:linear-gradient(90deg,#f1e6dc 0%,#f5ebe3 55%,#eadcd2 100%)}
.hero-photo{left:0;top:0;width:440px;height:400px;background:linear-gradient(120deg,#e9e6d8 0%,#c9c2d8 35%,#f2f0e6 70%,rgba(245,235,227,0))}
.hero-kicker{left:442px;top:113px;font-size:15px;letter-spacing:.3px}
.hero-title{left:442px;top:138px;font-size:32px;font-weight:500;line-height:41px;letter-spacing:1.3px;width:460px}
.btn{display:flex;align-items:center;justify-content:center;font-family:'Roboto',sans-serif;font-size:18px;letter-spacing:.8px;width:187px;height:47px}
.btn.dark{background:var(--dark-btn);color:var(--white);font-weight:500}
.btn.light{background:var(--light-btn);color:#333}
.about{left:122px;top:736px;width:656px;height:436px;border:3.5px solid #2a2a2a;text-align:center}
.about h1{font-family:'Roboto',sans-serif;font-weight:400;font-size:28px;line-height:34px;margin-top:22px}
.about .label{font-size:15px;letter-spacing:.5px;margin-top:74px;line-height:18px}
.about p{font-size:15px;line-height:20.4px;color:#333;width:550px;margin:0 auto;letter-spacing:.3px}
.about p+p{margin-top:20px}
.services{top:1224px;left:0;width:900px;height:483px;background:linear-gradient(90deg,#4a4a4c,#353537 50%,#3f4241);color:var(--white);text-align:center}
.services h2{font-size:20px;font-weight:500;letter-spacing:1.2px;line-height:27px;margin-top:70px}
.services .lead{font-weight:700;font-size:14px;line-height:18.2px;width:540px;margin:17px auto 0}
.services p{font-size:15px;line-height:20.2px;width:550px;margin:17px auto 0;letter-spacing:.3px}
.services .items p{margin-top:20px}
.cta{top:1707px;left:0;width:900px;height:375px;background:var(--sky);color:var(--white)}
.cta-photo{left:502px;top:0;width:398px;height:375px;background:radial-gradient(ellipse at 55% 60%,#b7ad9c 0%,#9f968a 35%,rgba(111,156,203,0) 70%)}
.cta h2{position:absolute;right:441px;top:38px;text-align:right;font-size:26px;font-weight:700;line-height:34px;letter-spacing:1.2px}
.cta h3{position:absolute;right:441px;top:170px;text-align:right;font-size:20px;font-weight:500;line-height:27px;letter-spacing:1.2px}
.footer{top:2082px;left:0;width:900px;height:158px;background:var(--footer);color:var(--white)}
.footer .brand-mark{background:var(--white);width:74px;height:74px}
.footer-contact{font-size:12.5px;line-height:1;display:flex;align-items:center;gap:10px;white-space:nowrap}
.copyright{top:2299px;left:0;width:1200px;text-align:center;font-size:12px;color:#333;letter-spacing:.3px}
</style>
</head>
<body>
<div class="abs flags">
  <div class="flag nl"><span style="background:#ae1c28"></span><span style="background:#fff"></span><span style="background:#21468b"></span></div>
  <div class="flag fr"><span style="background:#0055a4"></span><span style="background:#fff"></span><span style="background:#ef4135"></span></div>
</div>

<div class="site">
  <header>
    <div class="abs brand-mark" style="left:27px;top:32px"></div>
    <div class="abs brand-name" style="left:142px;top:52px;font-size:32px;line-height:34px">Rouwcentrum</div>
    <div class="abs brand-name" style="left:142px;top:90px;font-size:26px;line-height:30px">Verhaegen <span style="font-size:16px">bvba</span></div>

    <svg class="abs" style="left:473px;top:61px" width="18" height="20" viewBox="0 0 18 20"><path d="M4 2 L7 2 L8 6 L6 7.5 C7 10 8.5 12 11 13 L12.5 11 L16 12 L16 15 C16 16 15 17 14 17 C8 17 2 11 2 5 C2 3.5 3 2 4 2Z" fill="none" stroke="#1c1c1c" stroke-width="1.6"/><path d="M11 2 A5 5 0 0 1 16 7 M11 5 A2 2 0 0 1 13 7" fill="none" stroke="#1c1c1c" stroke-width="1.4"/></svg>
    <div class="abs contact-main" style="left:502px;top:62px">011 48 27 90</div>
    <div class="abs contact-sub" style="left:502px;top:86px">24/24, 7 op 7</div>

    <svg class="abs" style="left:684px;top:59px" width="14" height="20" viewBox="0 0 14 20"><path d="M7 1 C3.5 1 1 3.6 1 7 C1 11.5 7 19 7 19 C7 19 13 11.5 13 7 C13 3.6 10.5 1 7 1Z" fill="#1c1c1c"/><circle cx="7" cy="7" r="2.4" fill="#fff"/></svg>
    <div class="abs contact-main" style="left:708px;top:62px">Lindestraat 18</div>
    <div class="abs contact-sub" style="left:708px;top:86px">3700 Heerveld (Bovenrode)</div>

    <div class="abs rule" style="left:47px;top:202px;width:300px"></div>
    <div class="abs ornament" role="img" aria-label="Sierlijk krulornament" style="left:389px;top:167px;width:127px;height:51px"></div>
    <div class="abs rule" style="left:553px;top:202px;width:300px"></div>

    <nav class="abs nav">
      <a class="active" href="#" style="left:142px">Home</a>
      <a href="#" style="left:226px">Over ons</a>
      <a href="#" style="left:334px">Online Condoleren</a>
      <a href="#" style="left:516px">Bloemen bestellen</a>
      <a href="#" style="left:698px">Contact</a>
    </nav>
  </header>

  <section class="abs hero">
    <div class="abs hero-photo" role="img" aria-label="Boeket met witte lelies, margrieten en paarse bloemen"></div>
    <div class="abs hero-kicker">Rouwcentrum Verhaegen bvba:</div>
    <h1 class="abs hero-title">een persoonlijke service in afscheidsbegeleiding</h1>
    <div class="abs btn dark" style="left:441px;top:285px">011 48 27 90</div>
    <div class="abs btn light" style="left:666px;top:285px">CONTACTEER ONS</div>
  </section>

  <section class="abs about">
    <h1>Rouwcentrum Verhaegen,<br>een complete service in rouw- en<br>afscheidsbegeleiding</h1>
    <div class="ornament" role="img" aria-label="Sierlijk krulornament" style="position:absolute;left:280px;top:142px;width:90px;height:36px"></div>
    <div class="label">OVER ONS</div>
    <p>Afscheid nemen van een dierbare is één van de zwaarste dingen in een mensenleven. Rouwcentrum Verhaegen in Bovenrode neemt alle praktische en administratieve zaken die erbij komen kijken, voor u in handen. Zodat u in alle rust afscheid kunt nemen.</p>
    <p>Onze mensen hebben een ruime ervaring in afscheidsbegeleiding en staan 24 uur op 24 uur voor u klaar. Ons volledig gerenoveerde funerarium staat open voor u en uw kennissen, zodat u op elk moment van de dag uw dierbare kan groeten.</p>
  </section>

  <section class="abs services" role="region" aria-label="Organisatie uitvaart">
    <div class="ornament" role="img" aria-label="Lelie-embleem" style="position:absolute;left:430px;top:16px;width:40px;height:40px;background:#8a8a8c;opacity:.6"></div>
    <h2>ORGANISATIE UITVAART<br>EN EREDIENST</h2>
    <div class="lead">De organisatie van de uitvaartplechtigheid is een moment van bezinning, waar de persoonlijkheid van de overledene mooi in de verf gezet kan worden. Ons team staat u hierin bij en selecteert met u de mooiste teksten, liederen en foto’s om zo tot een gepast en waardig afscheid te komen.</div>
    <p>De uitvaart kan plaatsvinden in uw parochiekerk of onze aula als u dat wenst, die plaats biedt aan maximum 100 genodigden. We kunnen volgende zaken voor u regelen:</p>
    <div class="items">
      <p>gebedswake de avond voor de begrafenis</p>
      <p>gebedsdienst met priester (indien mogelijk)</p>
      <p>eucharistieviering met priester (op dinsdag en vrijdag<br>in de parochies van Bovenrode)</p>
    </div>
  </section>

  <section class="abs cta">
    <div class="abs cta-photo" role="img" aria-label="Stenen engelenbeeld tegen blauwe lucht"></div>
    <h2>HEBT U VRAGEN OF WILT U<br>ONS UITVAARTCENTRUM<br>INSCHAKELEN?</h2>
    <h3>CONTACTEER ONS<br>WE ZIJN ER VOOR U</h3>
    <div class="abs btn dark" style="left:274px;top:273px">011 48 27 90</div>
    <div class="abs btn light" style="left:274px;top:329px">CONTACTEER ONS</div>
  </section>

  <footer class="abs footer">
    <div class="abs brand-mark" style="left:256px;top:36px"></div>
    <div class="abs brand-name" style="left:351px;top:44px;font-size:32px;line-height:34px;color:#fff">Rouwcentrum</div>
    <div class="abs brand-name" style="left:351px;top:82px;font-size:26px;line-height:30px;color:#fff">Verhaegen <span style="font-size:16px">bvba</span></div>
    <div class="abs" style="left:598px;top:51px;width:1px;height:59px;background:#fff"></div>
    <div class="abs footer-contact" style="left:623px;top:53px">
      <svg width="13" height="10" viewBox="0 0 13 10"><rect x=".6" y=".6" width="11.8" height="8.8" fill="none" stroke="#fff" stroke-width="1.1"/><path d="M.6 .6 L6.5 5.5 L12.4 .6" fill="none" stroke="#fff" stroke-width="1.1"/></svg>
      <span>info@rouwcentrum-verhaegen.be</span>
    </div>
    <div class="abs footer-contact" style="left:623px;top:75px">
      <svg width="13" height="13" viewBox="0 0 18 20"><path d="M4 2 L7 2 L8 6 L6 7.5 C7 10 8.5 12 11 13 L12.5 11 L16 12 L16 15 C16 16 15 17 14 17 C8 17 2 11 2 5 C2 3.5 3 2 4 2Z" fill="#fff"/></svg>
      <span>011 48 27 90</span>
    </div>
    <div class="abs footer-contact" style="left:623px;top:98px">
      <svg width="13" height="13" viewBox="0 0 14 20"><path d="M7 1 C3.5 1 1 3.6 1 7 C1 11.5 7 19 7 19 C7 19 13 11.5 13 7 C13 3.6 10.5 1 7 1Z" fill="#fff"/><circle cx="7" cy="7" r="2.4" fill="#000"/></svg>
      <span>Lindestraat 18, 3700 Heerveld (Bovenrode)</span>
    </div>
  </footer>
</div>

<div class="abs copyright">2018 Webatelier Noord &nbsp;- Sitemap &nbsp;- Privacy Policy</div>
</body>
</html>
```